Danica Pruett Interiors business cards

We need a DOUBLE SIDED business card design that is simple, elegant and modern. We are a rapidly growing Interior Design Firm, and our brand colours are blush pink, navy, and antique gold, so we require some or all of these colours to be used. The final design should portray elegance, simplicity, and have a modern feel. We have upload inspiration photos that have the feel we're looking for.

Industry/Entity Type

Interior Design

Contact Information for Business Card

Contact information and LOGO

Colors
EB3D1F
EC4F4E
F09395
F8D3D4
FCEDEE

Requirements
Must have
• Navy, the right shade of blush pink, and antique gold

```html
<!DOCTYPE html>
<html lang="en">
<head>
<meta charset="utf-8">
<title>Danica Pruett Interiors — Business Card</title>
<link rel="stylesheet" href="https://fonts.googleapis.com/css2?family=Open+Sans:wght@400;700&display=swap">
<style>
  :root {
    --page: #ffffff;
    --blush: #fcedee;
    --coral: #eb5150;
    --navy: #1f2458;
    --gold: #9c7b4d;
    --light: #fcedee;
  }
  * { margin: 0; padding: 0; box-sizing: border-box; }
  html, body {
    width: 1200px; height: 900px; overflow: hidden;
    background: var(--page);
    font-family: "Open Sans", Arial, sans-serif;
  }
  .card {
    position: absolute;
    left: 263px;
    width: 675px; height: 405px;
    background: var(--blush);
    overflow: hidden;
    box-shadow: -4px 6px 10px rgba(0,0,0,0.25);
  }
  .card--front { top: 24px; }
  .card--back { top: 471px; }
  .card__waves { position: absolute; inset: 0; width: 100%; height: 100%; }
  .wave--coral { fill: var(--coral); }
  .wave--navy { fill: var(--navy); }
  .wave--gold { fill: var(--gold); }

  .wordmark {
    position: absolute;
    color: var(--gold);
    font-weight: 400;
    text-transform: uppercase;
    white-space: nowrap;
    transform: translateX(-50%);
    letter-spacing: 0.02em;
  }
  .card--front .wordmark { left: 337px; top: 183px; font-size: 24px; }
  .card--back .wordmark { left: 169px; top: 218px; font-size: 16px; }

  .identity {
    position: absolute;
    right: 53px; top: 149px;
    text-align: right;
    color: var(--light);
    font-weight: 700;
    text-transform: uppercase;
  }
  .identity__name { font-size: 27px; line-height: 1.1; }
  .identity__role { font-size: 15.5px; line-height: 1.2; }

  .contacts {
    position: absolute;
    right: 53px; top: 225px;
    list-style: none;
    color: var(--light);
    font-size: 16px;
  }
  .contacts__item {
    display: flex; align-items: center; justify-content: flex-end;
    height: 26.5px;
  }
  .contacts__icon {
    width: 20px; height: 20px; margin-left: 10px;
    fill: none; stroke: var(--light); stroke-width: 2;
  }
</style>
</head>
<body>

<section class="card card--front">
  <svg class="card__waves" viewBox="0 0 1125 675" preserveAspectRatio="none" aria-hidden="true">
    <path class="wave--coral" d="M0,505 C150,600 350,585 500,548 C700,500 850,455 1000,480 C1060,490 1100,520 1125,542 L1125,675 L0,675 Z"/>
    <path class="wave--navy" d="M0,438 C40,535 200,572 400,548 C250,585 80,572 0,495 Z"/>
    <path class="wave--gold" d="M715,476 C850,430 1000,432 1125,482 L1125,527 C1020,472 880,456 715,476 Z"/>
  </svg>
  <p class="wordmark">Danica Pruett Interiors</p>
</section>

<section class="card card--back">
  <svg class="card__waves" viewBox="0 0 1125 675" preserveAspectRatio="none" aria-hidden="true">
    <path class="wave--coral" d="M0,410 C80,490 180,515 280,513 C420,510 520,420 580,320 C660,190 760,130 890,132 C980,133 1060,170 1125,212 L1125,675 L0,675 Z"/>
    <path class="wave--navy" d="M0,320 C70,430 170,500 280,500 C430,500 545,380 578,248 C525,405 420,472 280,472 C170,472 70,405 0,350 Z"/>
    <path class="wave--gold" d="M580,295 C650,160 760,92 890,92 C990,92 1070,125 1125,158 L1125,190 C1060,150 990,120 890,120 C770,120 660,180 580,295 Z"/>
  </svg>
  <p class="wordmark">Danica Pruett Interiors</p>

  <div class="identity">
    <h1 class="identity__name">Danica Pruett</h1>
    <p class="identity__role">Principal Designer</p>
  </div>

  <ul class="contacts">
    <li class="contacts__item">905 555 0142
      <svg class="contacts__icon" viewBox="0 0 24 24" aria-hidden="true"><path d="M6 3 L9 3 L10 8 L8 10 C9 13 11 15 14 16 L16 14 L21 15 L21 18 C21 20 19 21 17 21 C10 20 4 14 3 7 C3 5 4 3 6 3 Z"/><path d="M15 4 C18 5 19 6 20 9"/><path d="M14 7 C16 7.5 16.5 8 17 10"/></svg>
    </li>
    <li class="contacts__item">danica@dpinteriorsinc.com
      <svg class="contacts__icon" viewBox="0 0 24 24" aria-hidden="true"><circle cx="12" cy="12" r="4"/><path d="M16 8 L16 14 C16 16 19 16 20 14 C22 9 19 3 12 3 C7 3 3 7 3 12 C3 17 7 21 12 21 C14 21 16 20 17 19"/></svg>
    </li>
    <li class="contacts__item">www.danicapruettinteriors.com
      <svg class="contacts__icon" viewBox="0 0 24 24" aria-hidden="true"><circle cx="12" cy="12" r="9"/><ellipse cx="12" cy="12" rx="4" ry="9"/><path d="M3 12 L21 12 M5 7 L19 7 M5 17 L19 17"/></svg>
    </li>
  </ul>
</section>

</body>
</html>
```